https://dorvakel.com

We need a cool technology design for our Managed IT Services company. We are located in Coral Springs Florida. We provide all IT services and support for small to medium sized businesses. We would like to see designs that use our blue and white colors from our website.

```html
<!DOCTYPE html>
<html lang="en">
<head>
<meta charset="UTF-8">
<title>Dorvakel Business Card</title>
<link href="https://fonts.googleapis.com/css2?family=Lato:wght@400;700;900&display=swap" rel="stylesheet">
<style>
  :root {
    --backdrop: #262627;
    --card: #1b1b1c;
    --card-edge: #232324;
    --white: #ffffff;
    --soft-white: #e6e6e6;
    --blue: #1d86d4;
    --blue-light: #3a9be3;
    --divider: #8a8a8a;
  }
  * { margin: 0; padding: 0; box-sizing: border-box; }
  html, body {
    width: 1200px;
    height: 900px;
    overflow: hidden;
    background: var(--backdrop);
    font-family: "Lato", sans-serif;
  }
  .canvas {
    position: relative;
    width: 1200px;
    height: 900px;
  }
  .card {
    position: absolute;
    width: 665px;
    height: 380px;
    background: var(--card);
    border-radius: 16px;
    box-shadow: 0 18px 40px rgba(0,0,0,0.55);
    border: 1px solid var(--card-edge);
    overflow: hidden;
  }
  .card-front { left: 110px; top: 45px; }
  .card-back { left: 425px; top: 470px; }

  .wordmark {
    font-family: "Lato", sans-serif;
    font-weight: 900;
    color: var(--white);
    letter-spacing: 0.02em;
    display: flex;
    align-items: center;
    gap: 14px;
    line-height: 1;
  }
  .wordmark-dot {
    width: 14px;
    height: 14px;
    border-radius: 50%;
    background: var(--blue);
  }

  .card-front .wordmark {
    position: absolute;
    left: 0; right: 0;
    top: 138px;
    justify-content: center;
    font-size: 70px;
  }
  .front-url {
    position: absolute;
    left: 0; right: 0;
    top: 268px;
    text-align: center;
    color: var(--white);
    font-size: 13px;
    font-weight: 700;
    letter-spacing: 0.32em;
  }

  .back-brand {
    position: absolute;
    left: 0;
    width: 330px;
    top: 0;
    height: 100%;
    display: flex;
    align-items: center;
    justify-content: center;
  }
  .back-brand .wordmark { font-size: 44px; gap: 10px; }
  .back-brand .wordmark-dot { width: 10px; height: 10px; }

  .divider {
    position: absolute;
    left: 340px;
    top: 55px;
    width: 1.5px;
    height: 240px;
    background: linear-gradient(to bottom, rgba(138,138,138,0), var(--divider) 35%, var(--divider) 65%, rgba(138,138,138,0));
  }

  .contact {
    position: absolute;
    left: 372px;
    top: 92px;
    color: var(--soft-white);
  }
  .contact-name {
    font-size: 19px;
    color: var(--blue);
    letter-spacing: 0.03em;
    text-transform: uppercase;
  }
  .contact-name .first { font-weight: 400; color: var(--blue-light); }
  .contact-name .last { font-weight: 700; }
  .contact-title {
    font-size: 13px;
    margin-top: 3px;
    color: var(--white);
  }
  .contact-list {
    list-style: none;
    margin-top: 30px;
  }
  .contact-list li {
    display: flex;
    align-items: center;
    gap: 12px;
    font-size: 14px;
    color: var(--white);
    margin-bottom: 13px;
  }
  .contact-list svg {
    width: 13px;
    height: 13px;
    fill: var(--blue);
    flex: none;
  }
</style>
</head>
<body>
<main class="canvas">

  <section class="card card-front">
    <div class="wordmark"><span class="wordmark-dot"></span>DORVAKEL</div>
    <p class="front-url">www.dorvakel.com</p>
  </section>

  <section class="card card-back">
    <div class="back-brand">
      <div class="wordmark"><span class="wordmark-dot"></span>DORVAKEL</div>
    </div>
    <div class="divider"></div>
    <div class="contact">
      <p class="contact-name"><span class="first">Mirela</span> <span class="last">Okonjo</span></p>
      <p class="contact-title">Managing Director</p>
      <ul class="contact-list">
        <li>
          <svg viewBox="0 0 16 16" aria-hidden="true"><path d="M3 1h3l1.5 4-2 1.3a9 9 0 0 0 4.2 4.2L11 8.5l4 1.5v3a2 2 0 0 1-2 2A13 13 0 0 1 1 3a2 2 0 0 1 2-2z"/></svg>
          <span>+61 02 5550 1847</span>
        </li>
        <li>
          <svg viewBox="0 0 16 16" aria-hidden="true"><path d="M1 3h14v10H1z M1.5 3.5 8 9l6.5-5.5" /><path d="M1 3l7 6 7-6v1L8 10 1 4z" fill="#1b1b1c"/></svg>
          <span>+61 0400 555 316</span>
        </li>
        <li>
          <svg viewBox="0 0 16 16" aria-hidden="true"><circle cx="8" cy="8" r="7"/><path d="M1 8h14M8 1c-3 3.5-3 10.5 0 14M8 1c3 3.5 3 10.5 0 14" stroke="#1b1b1c" stroke-width="1.1" fill="none"/></svg>
          <span>mirela@dorvakel.com</span>
        </li>
      </ul>
    </div>
  </section>

</main>
</body>
</html>
```